Baby Muslin Wrap/Swaddle Box Packaging Design

We are a company that sells baby muslin wraps. We currently sell cotton and bamboo baby muslin wraps in egdy, monochrome designs. We are looking for new packaging designs and would like this new packaging to consist of a box with a window at the front to see and feel muslin wrap. Each box will hold one wrap (please see some examples of style of box we are after attached). Our logo (Ned and Rosie) should be on the front of the box. We are open to any colour options/illustrations on the box but would like it to stand out if placed on a shelf in a store. We would be interested in seeing a white box with monochrome designs across box.. Gold writing would also be great to see. There will be some additional info that will need to go on the back of the box.
Target Market(s)
women 20-40 year of age.
Industry/Entity Type
Baby
Requirements
Must have
- Logo
- Box design with window

```html
<!DOCTYPE html>
<html lang="en">
<head>
<meta charset="UTF-8">
<title>Ned and Rosie – Swaddle Box</title>
<link href="https://fonts.googleapis.com/css2?family=Dancing+Script:wght@500&family=Cinzel:wght@500&family=Ruge+Boogie&family=Arimo&display=swap" rel="stylesheet">
<style>
  :root {
    --page: #ffffff;
    --box-blue: #c5e4ea;
    --band: #d9e9dc;
    --band-line: #e9d6e6;
    --window: #ffffff;
    --teal: #4fa4aa;
    --red: #e85a5c;
    --purple: #a980c8;
    --pink: #e07c94;
    --small-text: #e9a36a;
    --skin: #f3d7c8;
  }
  html, body {
    margin: 0;
    padding: 0;
    width: 1200px;
    height: 939px;
    overflow: hidden;
    background: var(--page);
  }
  .canvas {
    position: relative;
    width: 1200px;
    height: 939px;
  }
  .panel {
    position: absolute;
    top: 61px;
    height: 796px;
    background: var(--box-blue);
  }
  .panel--side { left: 95px; width: 173px; }
  .panel--front { left: 298px; width: 800px; }

  .dot-band {
    position: absolute;
    inset: 14px;
    border: 8px solid var(--band);
    outline: 2px solid var(--band-line);
    outline-offset: -5px;
  }

  .window {
    position: absolute;
    left: 70px;
    top: 70px;
    width: 330px;
    height: 600px;
    background: var(--window);
    border-radius: 26px;
  }
  .babies-art {
    position: absolute;
    left: 108px;
    top: 44px;
    width: 250px;
    height: 84px;
    border-radius: 42px 42px 0 0;
    background: linear-gradient(180deg, var(--skin), #ffffff);
  }
  .fabric-note {
    position: absolute;
    left: 70px;
    top: 690px;
    width: 330px;
    margin: 0;
    text-align: center;
    font: 15px/18px "Arimo", sans-serif;
    color: var(--small-text);
  }

  .brand {
    position: absolute;
    display: flex;
    align-items: center;
    gap: 10px;
    font-family: "Dancing Script", cursive;
    font-weight: 500;
    color: var(--teal);
    white-space: nowrap;
  }
  .brand__dot {
    border-radius: 50%;
    background: var(--pink);
  }
  .panel--front .brand { left: 460px; top: 220px; font-size: 50px; }
  .panel--front .brand__dot { width: 18px; height: 18px; }
  .panel--side .brand { left: 0; width: 173px; justify-content: center; top: 150px; font-size: 22px; gap: 5px; }
  .panel--side .brand__dot { width: 8px; height: 8px; }

  .tagline {
    position: absolute;
    left: 0;
    right: 0;
    text-align: center;
    margin: 0;
    white-space: nowrap;
  }
  .tagline--beautiful { font-family: "Dancing Script", cursive; font-weight: 500; color: var(--red); }
  .tagline--swaddle { font-family: "Cinzel", serif; font-weight: 500; color: var(--teal); letter-spacing: 2px; }
  .tagline--muslin { font-family: "Ruge Boogie", cursive; color: var(--purple); }

  .front-copy { position: absolute; left: 460px; width: 300px; top: 0; height: 100%; }
  .front-copy .tagline--beautiful { top: 418px; font-size: 50px; }
  .front-copy .tagline--swaddle { top: 508px; font-size: 44px; }
  .front-copy .tagline--muslin { top: 612px; font-size: 58px; }

  .side-copy .tagline--beautiful { top: 335px; font-size: 26px; }
  .side-copy .tagline--swaddle { top: 395px; font-size: 24px; }
  .side-copy .tagline--muslin { top: 455px; font-size: 28px; }
</style>
</head>
<body>
<div class="canvas">
  <section class="panel panel--side">
    <div class="brand"><span>Ned and Rosie</span><span class="brand__dot"></span></div>
    <div class="side-copy">
      <p class="tagline tagline--beautiful">Beautiful</p>
      <p class="tagline tagline--swaddle">SWADDLE</p>
      <p class="tagline tagline--muslin">Muslin Wrap</p>
    </div>
  </section>

  <section class="panel panel--front">
    <div class="dot-band"></div>
    <div class="window"></div>
    <div class="babies-art" role="img" aria-label="Illustration of two sleeping swaddled babies peeking over the window"></div>
    <div class="brand"><span>Ned and Rosie</span><span class="brand__dot"></span></div>
    <div class="front-copy">
      <p class="tagline tagline--beautiful">Beautiful</p>
      <p class="tagline tagline--swaddle">SWADDLE</p>
      <p class="tagline tagline--muslin">Muslin Wrap</p>
    </div>
    <p class="fabric-note">100% Cotton (120 x 120 cm)<br>pre-whased</p>
  </section>
</div>
</body>
</html>
```